Business Card Design

We are a flooring/granite/cabinet company
want a sleek and modern design card. Will send our logo. maybe our logo in 3d on card.
black card

Industry/Entity Type

Business

Contact Information for Business Card

Gregory Tallis
company name Stone Hearth Depot
4827 fm 71s 78540
210-634-8872
stonehearthdepot@mailvista.example

```html
<!DOCTYPE html>
<html lang="en">
<head>
<meta charset="utf-8">
<title>Stone Hearth Depot – Business Card</title>
<link rel="stylesheet" href="https://fonts.googleapis.com/css2?family=Noto+Sans:wght@400;700&display=swap">
<style>
  :root {
    --backdrop: #6f5b48;
    --card-black: #050508;
    --card-glow: #141a2e;
    --tile: #e4e6e8;
    --tile-edge: #c9ccd0;
    --text-light: #ffffff;
    --brand-steel: #5d7290;
    --brand-deep: #2c4866;
    --marble-light: #f4f5f6;
    --marble-mid: #d8dbde;
    --photo-frame: #ffffff;
  }
  * { margin: 0; padding: 0; box-sizing: border-box; }
  html, body { width: 900px; height: 1200px; overflow: hidden; }
  body {
    position: relative;
    background: var(--backdrop);
    font-family: "Noto Sans", Tahoma, sans-serif;
  }
  .card {
    position: absolute;
    left: 26px;
    width: 844px;
    height: 493px;
    overflow: hidden;
    box-shadow: 0 4px 14px rgba(0,0,0,0.45);
  }
  .card-front {
    top: 95px;
    background: radial-gradient(ellipse 60% 55% at 60% 45%, var(--card-glow) 0%, var(--card-black) 75%);
  }
  .card-back {
    top: 615px;
    background: linear-gradient(135deg, var(--marble-light) 0%, var(--marble-mid) 35%, var(--marble-light) 55%, var(--marble-mid) 80%, var(--marble-light) 100%);
  }
  .tile {
    position: absolute;
    width: 72px;
    height: 70px;
    background: linear-gradient(135deg, #f2f3f4 0%, var(--tile) 50%, var(--tile-edge) 100%);
    box-shadow: 0 2px 4px rgba(0,0,0,0.6);
  }
  .brand {
    position: absolute;
    display: flex;
    align-items: center;
    gap: 14px;
    font-weight: 700;
    letter-spacing: 1px;
    text-transform: uppercase;
    white-space: nowrap;
  }
  .brand-mark {
    width: 22px;
    height: 22px;
    background: currentColor;
  }
  .card-front .brand {
    right: 30px;
    top: 120px;
    font-size: 34px;
    color: var(--brand-steel);
  }
  .card-back .brand {
    left: 0;
    right: 0;
    top: 170px;
    justify-content: center;
    font-size: 38px;
    color: var(--brand-deep);
  }
  .contact {
    position: absolute;
    left: 34px;
    top: 333px;
    color: var(--text-light);
  }
  .contact-name { font-size: 30px; line-height: 1.2; margin-bottom: 8px; }
  .contact-line {
    font-size: 19px;
    line-height: 1.2;
    display: flex;
    align-items: center;
    gap: 10px;
    margin-bottom: 9px;
  }
  .contact-line svg { width: 19px; height: 19px; flex: none; }
  .photo {
    position: absolute;
    top: 307px;
    height: 150px;
    border: 3px solid var(--photo-frame);
    box-shadow: 0 2px 6px rgba(0,0,0,0.35);
  }
  .photo-slab { left: 30px; width: 262px; background: linear-gradient(135deg, #cfd0d2, #8e9094); }
  .photo-floor { left: 291px; width: 262px; background: linear-gradient(160deg, #4a3a2c, #8a6a48 60%, #b89468); }
  .photo-kitchen { left: 552px; width: 262px; background: linear-gradient(180deg, #d2a464 0%, #b57f3c 55%, #1c1c1c 70%, #c99858 100%); }
</style>
</head>
<body>
  <section class="card card-front">
    <div class="tile-pattern" role="img" aria-label="Checkerboard of white marble tiles">
      <div class="tile" style="left:0;top:0"></div>
      <div class="tile" style="left:144px;top:0"></div>
      <div class="tile" style="left:72px;top:70px"></div>
      <div class="tile" style="left:216px;top:70px"></div>
      <div class="tile" style="left:0;top:141px"></div>
      <div class="tile" style="left:144px;top:141px"></div>
      <div class="tile" style="left:72px;top:211px"></div>
    </div>

    <div class="brand"><span class="brand-mark"></span>Stone Hearth Depot</div>

    <div class="contact">
      <p class="contact-name">Gregory Tallis</p>
      <p class="contact-line">4827 fm 71s 78540</p>
      <p class="contact-line">
        <svg viewBox="0 0 20 20" aria-hidden="true"><rect width="20" height="20" rx="4" fill="#fff"/><path d="M6 4.5l2.2 0 1 3-1.4 1.2a8 8 0 0 0 3.5 3.5l1.2-1.4 3 1v2.2c0 .8-.7 1.5-1.5 1.5A10.5 10.5 0 0 1 4.5 6c0-.8.7-1.5 1.5-1.5z" fill="#050508"/></svg>
        210-634-8872
      </p>
      <p class="contact-line">
        <svg viewBox="0 0 20 20" aria-hidden="true"><rect width="20" height="20" rx="4" fill="#fff"/><rect x="4" y="6" width="12" height="8" fill="none" stroke="#050508" stroke-width="1.5"/><path d="M4 6l6 5 6-5" fill="none" stroke="#050508" stroke-width="1.5"/></svg>
        stonehearthdepot@mailvista.example
      </p>
    </div>
  </section>

  <section class="card card-back" role="img" aria-label="White marble surface with grey veining">
    <div class="brand"><span class="brand-mark"></span>Stone Hearth Depot</div>
    <div class="photo photo-slab" role="img" aria-label="Photo of polished grey granite slabs"></div>
    <div class="photo photo-floor" role="img" aria-label="Photo of a living room with brown stone tile floor"></div>
    <div class="photo photo-kitchen" role="img" aria-label="Photo of a kitchen with oak cabinets and black countertops"></div>
  </section>
</body>
</html>
```